Business card website / business card for website

We are a French website selling products Made in USA of quality, we need a business card to give from hand to hand and for deposit in the cartons of Each order. We-have the logo That I send in the attachments The theme is: US Vintage and find the compromised entre les national park ambience us and the atmosphere Brooklyn If you can make the feeling it's great The site www.latablederivebleue.com (opening April) You can change the logo a little gold in color it could ... we are a French website selling products Made in USA quality, we need a business card to give from hand to hand and deposit in cartons each order. we have the logo that I convey in the attached parts is the theme: Vintage embiance US and find a compromise between the atmosphere us national park and the atmosphere Brooklyn at: www.latablederivebleue.com (opening April) if you can the impression is great

Target Market(s)

25-50 YEARS man, woman.

Industry/Entity Type

Business

Contact Information for Business Card

www.latablederivebleue.com
N'oubliez pas que nous sommes là si vous avez besoin de nouscontact@latablederivebleue.com

Font styles to use
Serif

Requirements
Must have
• my logo with "general store", my email address preceded by the phrase: Do not forget that we are here if you need us My logo with the words "general store," my email address Preceded by the sentence: remember we're here if you need us (in french)
Nice to have
• i like this style: http://designcorbel.net/ideas/print-ideas/25-charming-old-style-business-card-designs/ must feel the Vintage America it must feel the Vintage America lice can change a little logo or to color ... You can change the logo a little gold in color it could ... i like kraft paper with red ....
Should not have

```html
<!DOCTYPE html>
<html lang="fr">
<head>
<meta charset="utf-8">
<title>La Table de Rive Bleue – Carte de visite</title>
<link rel="stylesheet" href="https://fonts.googleapis.com/css2?family=Marcellus+SC&family=Tinos:ital@0;1&display=swap">
<style>
  :root {
    --backdrop: #ebebea;
    --cream: #ebdfc2;
    --cream-deep: #e1d4b4;
    --ink: #2b2826;
    --line: #cbbf9f;
  }
  * { box-sizing: border-box; margin: 0; padding: 0; }
  html, body { width: 1006px; height: 1200px; overflow: hidden; }
  body { background: var(--backdrop); position: relative; font-family: "Tinos", serif; color: var(--ink); }

  .card {
    position: absolute;
    width: 709px;
    border-radius: 30px;
    background: var(--cream);
    overflow: hidden;
    box-shadow: 0 14px 30px rgba(0,0,0,0.14), 0 2px 6px rgba(0,0,0,0.08);
  }
  .card--front { left: 137px; top: 141px; height: 409px; }
  .card--back  { left: 141px; top: 646px; height: 406px; }

  /* front */
  .brand-mark {
    position: absolute;
    left: 38px; top: 95px;
    width: 194px; height: 194px;
    border-radius: 50%;
    border: 2px solid var(--ink);
    display: flex; align-items: center; justify-content: center;
    text-align: center;
  }
  .brand-name {
    font-family: "Marcellus SC", serif;
    font-size: 21px;
    line-height: 1.2;
    color: var(--ink);
  }
  .front-info {
    position: absolute;
    left: 260px; width: 380px; top: 56px;
    text-align: center;
  }
  .store-title {
    font-family: "Marcellus SC", serif;
    font-size: 31px;
    letter-spacing: 0.5px;
    font-weight: 400;
  }
  .website { margin-top: 32px; font-size: 25px; }
  .email { margin-top: 14px; font-size: 21px; }
  .tagline { margin-top: 22px; font-size: 17px; font-style: italic; line-height: 27px; }

  .stripe-band {
    position: absolute;
    left: 0; right: 0; top: 306px; bottom: 0;
    background: var(--ink);
    border-top: 6px solid var(--cream-deep);
  }

  /* back */
  .stripe-field {
    position: absolute;
    left: 0; right: 0; top: 202px; bottom: 0;
    background: var(--cream-deep);
    border-top: 1px solid var(--line);
  }
  .back-frame { position: absolute; inset: 0; }
  .badge {
    position: absolute;
    left: 218px; top: 19px;
    width: 276px; height: 276px;
    border-radius: 50%;
    background: var(--ink);
    display: flex; align-items: center; justify-content: center;
    text-align: center;
  }
  .badge .brand-name { color: var(--cream); font-size: 25px; }
  .store-title--large {
    position: absolute;
    left: 0; right: 0; top: 285px;
    text-align: center;
    font-size: 60px;
    letter-spacing: -1px;
  }
</style>
</head>
<body>

<section class="card card--front" aria-label="Recto">
  <div class="brand-mark">
    <p class="brand-name">La Table<br>de Rive Bleue</p>
  </div>
  <div class="front-info">
    <h1 class="store-title">Général Store</h1>
    <p class="website">www.latablederivebleue.com</p>
    <p class="email">contact@latablederivebleue.com</p>
    <p class="tagline">N'oubliez pas que nous sommes ici si vous<br>avez besoin de nous</p>
  </div>
  <div class="stripe-band" role="img" aria-label="Bande décorative à rayures verticales sombres"></div>
</section>

<section class="card card--back" aria-label="Verso">
  <div class="stripe-field" role="img" aria-label="Motif décoratif de fines rayures verticales"></div>
  <svg class="back-frame" width="709" height="406" viewBox="0 0 709 406" aria-hidden="true">
    <circle cx="356" cy="157" r="150" fill="var(--cream)" stroke="var(--line)" stroke-width="2"/>
  </svg>
  <div class="badge">
    <p class="brand-name">La Table<br>de Rive Bleue</p>
  </div>
  <h2 class="store-title store-title--large">Général Store</h2>
</section>

</body>
</html>
```